AI Business Tools Landing Page

My web-based website builder (Nurvanta.com) will be adding many new features in the very near future and I need an eye-catching landing page to promote these new products.

The page will have a primary section of the 8 main products we are promoting:
1. AI Instant Website Generator
2. AI Chatbot
3. Online Store Builder with AI Assistance
4. AI Auto-Blogging System
5. Online Scheduling System
6. Custom Email System
7. SEO Service
8. CRM System

The page will also have a smaller section for links to our affiliate programs. These can be smaller, less-promanent buttons or links. These are the affiliate products:
1. Get Your LLC
2. Website Design and Maintenance
3. Tavolin Ads Management
4. Social Media Posting Service
5. Logo Design
6. Trademark Registration
7. Patent Application
8. Printing Services (including postcards, flyers, and merch.)
9. Bulk AI Content Generator

The theme and color scheme of the page should follow the theme of our main website, which is https://nurvanta.com.

I need the page fully coded and ready to deploy on my server.

I look forward to seeing your amazing designs!

```html
<!DOCTYPE html>
<html lang="en">
<head>
<meta charset="UTF-8">
<title>Nurvanta – The Premier AI Website Builder</title>
<link href="https://fonts.googleapis.com/css2?family=Poppins:wght@500;600;700&family=Source+Sans+3:wght@300;400&display=swap" rel="stylesheet">
<style>
  :root {
    --navy: #0b1a33;
    --navy-deep: #071225;
    --ink: #0f2540;
    --text: #333a44;
    --muted: #3d4550;
    --blue: #1a8fe3;
    --blue-dark: #1b6fd6;
    --green: #7dd8a4;
    --page: #f3f6fa;
    --white: #ffffff;
    --footer: #1f2c3d;
  }
  * { box-sizing: border-box; margin: 0; padding: 0; }
  html, body { width: 1200px; height: 2571px; overflow: hidden; }
  body { font-family: "Source Sans 3", sans-serif; color: var(--text); background: var(--page); }

  /* Hero */
  .hero { position: relative; height: 622px; background: radial-gradient(ellipse at 30% 40%, #12284a 0%, var(--navy) 55%, var(--navy-deep) 100%); overflow: hidden; }
  .hero-visual { position: absolute; left: 560px; top: 130px; width: 640px; height: 492px;
    background: radial-gradient(ellipse at 45% 75%, #c9a58a 0%, #4a5a78 22%, #1f4a86 40%, #10284d 70%, transparent 100%); }
  .brand { position: absolute; left: 112px; top: 25px; display: flex; align-items: center; gap: 18px; }
  .brand-dot { width: 62px; height: 62px; border-radius: 50%; background: var(--blue); }
  .brand-name { font-family: "Poppins", sans-serif; font-weight: 500; font-size: 38px; color: var(--white); }
  .btn-green { background: var(--green); color: var(--white); font-family: "Poppins", sans-serif; font-weight: 600; text-decoration: none; display: flex; align-items: center; justify-content: center; }
  .nav-cta { position: absolute; left: 933px; top: 28px; width: 157px; height: 58px; border-radius: 4px; font-size: 17px; }
  .hero-title { position: absolute; left: 109px; top: 202px; font-family: "Poppins", sans-serif; font-weight: 700; font-size: 48px; line-height: 58px; color: var(--white); }
  .hero-sub { position: absolute; left: 109px; top: 353px; font-size: 22px; font-weight: 300; color: var(--white); }
  .signup { position: absolute; left: 112px; top: 422px; display: flex; height: 57px; }
  .signup input { width: 283px; border: 0; border-radius: 4px 0 0 4px; padding: 0 16px; font-family: "Source Sans 3", sans-serif; font-size: 19px; font-weight: 300; color: #555; }
  .signup input::placeholder { color: #666; }
  .signup .btn-green { width: 233px; border: 0; border-radius: 0 4px 4px 0; font-size: 16px; }

  /* Features */
  .features { height: 1213px; padding-top: 86px; }
  .section-title { font-family: "Poppins", sans-serif; font-weight: 600; font-size: 39px; color: var(--ink); text-align: center; }
  .feature-grid { position: absolute; left: 112px; top: 816px; display: grid; grid-template-columns: repeat(4, 233px); grid-template-rows: 441px 459px; column-gap: 15.7px; row-gap: 19px; }
  .feature-card { background: var(--white); border-radius: 8px; box-shadow: 0 4px 18px rgba(20,40,80,.06); padding: 18px 10px 0; text-align: center; }
  .feature-icon { width: 100px; height: 96px; display: block; margin: 0 auto; }
  .feature-card h3 { font-family: "Poppins", sans-serif; font-weight: 600; font-size: 18px; line-height: 22px; color: var(--ink); margin: 14px 0 22px; }
  .feature-card p { font-size: 15.5px; font-weight: 300; line-height: 23.3px; color: var(--muted); }
  .tick { color: var(--blue-dark); font-weight: 700; margin-right: 6px; }

  /* Tools */
  .tools { position: relative; height: 640px; background: linear-gradient(135deg, #2a8ee0 0%, #2e86e2 50%, #2a7ad9 100%); }
  .tools .section-title { color: var(--white); font-size: 39px; line-height: 46px; padding-top: 85px; }
  .tool-link { position: absolute; width: 230px; height: 88px; background: var(--white); border-radius: 14px; display: flex; flex-direction: column; align-items: center; justify-content: center; text-align: center; text-decoration: none; font-family: "Poppins", sans-serif; font-weight: 500; font-size: 20px; line-height: 27px; color: #333; }
  .tool-link small { font-family: "Poppins", sans-serif; font-weight: 400; font-size: 15px; line-height: 24px; color: #444; }

  .footer { height: 96px; background: var(--footer); display: flex; align-items: center; justify-content: center; gap: 8px; color: var(--white); font-size: 16px; }
  .footer-dot { width: 20px; height: 20px; border-radius: 50%; background: var(--blue); }
  .footer-name { font-family: "Source Sans 3", sans-serif; font-weight: 400; font-size: 17px; }
</style>
</head>
<body>
<header class="hero">
  <div class="hero-visual" role="img" aria-label="Hand holding a smartphone with glowing AI interface panels floating above it"></div>
  <a class="brand" href="https://nurvanta.com"><span class="brand-dot"></span><span class="brand-name">Nurvanta</span></a>
  <a class="btn-green nav-cta" href="#">GET YOUR LLC</a>
  <h1 class="hero-title">The Premier AI<br>Website Builder</h1>
  <p class="hero-sub">Generate your site now!</p>
  <form class="signup"><input type="email" placeholder="Email Address"><button class="btn-green" type="submit">BUILD MY FREE WEBSITE</button></form>
</header>

<section class="features">
  <h2 class="section-title">Additional Features for Your Website</h2>
  <div class="feature-grid">
    <article class="feature-card">
      <svg class="feature-icon" viewBox="0 0 100 96" fill="none" stroke="#1a8fe3" stroke-width="3"><rect x="12" y="6" width="76" height="76" rx="3"/><line x1="12" y1="18" x2="88" y2="18"/><rect x="22" y="28" width="58" height="46"/><line x1="48" y1="42" x2="72" y2="42"/><line x1="48" y1="52" x2="72" y2="52"/><line x1="30" y1="62" x2="72" y2="62"/></svg>
      <h3>AI Instant Website<br>Generator</h3>
      <p><span class="tick">✔</span>Get a professional, SEO-optimized website in seconds!<br><span class="tick">✔</span>Includes custom domain, secure high-speed hosting, professional images, and more!</p>
    </article>
    <article class="feature-card">
      <svg class="feature-icon" viewBox="0 0 100 96" fill="none" stroke="#1a8fe3" stroke-width="3"><rect x="6" y="16" width="54" height="40" rx="8"/><line x1="16" y1="28" x2="46" y2="28"/><line x1="16" y1="38" x2="40" y2="38"/><rect x="40" y="46" width="52" height="38" rx="14"/><circle cx="56" cy="64" r="4"/><circle cx="76" cy="64" r="4"/></svg>
      <h3>AI<br>ChatBot</h3>
      <p><span class="tick">✔</span>Fully-trainable ChatBot will learn about your business to automate the customer support process!<br><span class="tick">✔</span>Built-in CRM features integrate emailing, text messaging, and contact forms!</p>
    </article>
    <article class="feature-card">
      <svg class="feature-icon" viewBox="0 0 100 96" fill="none" stroke="#1a8fe3" stroke-width="3"><rect x="10" y="8" width="80" height="70" rx="3"/><line x1="10" y1="22" x2="90" y2="22"/><path d="M20 38h8l6 20h20l4-14H32"/><circle cx="36" cy="66" r="3"/><circle cx="52" cy="66" r="3"/><line x1="64" y1="40" x2="82" y2="40"/><line x1="64" y1="50" x2="82" y2="50"/><path d="M70 62l14 6-6 2-2 6z"/></svg>
      <h3>Online Store Builder<br>with AI Assistance</h3>
      <p><span class="tick">✔</span>Sell you products online and integrate your products into any website!<br><span class="tick">✔</span>Accept payments from multiple payment gateways including Payvora and Quillpay!</p>
    </article>
    <article class="feature-card">
      <svg class="feature-icon" viewBox="0 0 100 96" fill="none" stroke="#1a8fe3" stroke-width="3"><rect x="22" y="4" width="56" height="76"/><line x1="32" y1="18" x2="68" y2="18"/><line x1="32" y1="28" x2="68" y2="28"/><line x1="32" y1="38" x2="68" y2="38"/><line x1="32" y1="48" x2="56" y2="48"/><path d="M22 40l-8 10v32M78 56l8 26"/><path d="M52 82l4-22 10 4-2 18"/></svg>
      <h3>AI Auto-Blogging<br>System</h3>
      <p><span class="tick">✔</span>AI will generate an incredible blog for y our business in seconds and immediately begin posting content for you!<br><span class="tick">✔</span>Choose from daily, weekly, or monthly automated blog posting. Consistent, unique, SEO-optimized content posting on cruise control!</p>
    </article>
    <article class="feature-card">
      <svg class="feature-icon" viewBox="0 0 100 96" fill="none" stroke="#1a8fe3" stroke-width="3"><rect x="20" y="4" width="56" height="72"/><rect x="28" y="16" width="8" height="8"/><rect x="28" y="32" width="8" height="8"/><rect x="28" y="48" width="8" height="8"/><line x1="42" y1="20" x2="66" y2="20"/><line x1="42" y1="36" x2="66" y2="36"/><line x1="42" y1="52" x2="58" y2="52"/><path d="M50 46l14 6-6 2-2 6z"/><line x1="8" y1="84" x2="92" y2="84"/><path d="M14 84V30h6M86 84V30h-10"/></svg>
      <h3>Online Scheduling<br>System</h3>
      <p><span class="tick">✔</span>Get appointment bookings, restaurant reservations, or consultations scheduled directly from your website!<br><span class="tick">✔</span>Manage your employees’ schedules and all you appointments from a simple, user-friendly dashboard!</p>
    </article>
    <article class="feature-card">
      <svg class="feature-icon" viewBox="0 0 100 96" fill="none" stroke="#1a8fe3" stroke-width="3"><path d="M8 16h84v50H34l-10 14v-14H8z"/><rect x="18" y="30" width="64" height="14" rx="3"/><text x="22" y="41" font-size="11" fill="#1a8fe3" stroke="none" font-family="Poppins, sans-serif">www.</text></svg>
      <h3>Custom emails using<br>your domain</h3>
      <p><span class="tick">✔</span>Quickly set up emails for yourself and all your employees with your own domain extension (example– johnd@yoursite.com). No more unprofessional Mailora and Inbexa email addresses!<br><span class="tick">✔</span>Manage all your business emails from a simple, user-friendly interface!</p>
    </article>
    <article class="feature-card">
      <svg class="feature-icon" viewBox="0 0 100 96" fill="none" stroke="#1a8fe3" stroke-width="3"><circle cx="50" cy="46" r="42"/><path d="M40 58l-8 8a8 8 0 0 1-11-11l10-10a8 8 0 0 1 11 0"/><path d="M60 34l8-8a8 8 0 0 1 11 11l-10 10a8 8 0 0 1-11 0"/><line x1="42" y1="54" x2="58" y2="38"/><path d="M26 30a28 28 0 0 1 40-10M74 62a28 28 0 0 1-40 10"/></svg>
      <h3>SEO Service–Automatic<br>Backlink Building</h3>
      <p><span class="tick">✔</span>Let us do the hard work of getting high-quality backlinks to your website. Although difficult to get, backlinks to your website boost search engine ranking more than any other strategy!<br><span class="tick">✔</span>Subscribe now and start getting 10-20 high-quality permanent backlinks to your website every</p>
    </article>
    <article class="feature-card">
      <svg class="feature-icon" viewBox="0 0 100 96" fill="none" stroke="#1a8fe3" stroke-width="3"><rect x="28" y="34" width="44" height="40" rx="3"/><circle cx="50" cy="52" r="8"/><path d="M38 72a12 12 0 0 1 24 0"/><path d="M50 34V10M28 46H12M72 46h16M36 34V22H22M64 34V22h14"/><rect x="46" y="4" width="8" height="8"/><rect x="4" y="42" width="8" height="8"/><rect x="88" y="42" width="8" height="8"/><rect x="14" y="18" width="8" height="8"/><rect x="78" y="18" width="8" height="8"/></svg>
      <h3>Customer Relationship<br>Management System</h3>
      <p><span class="tick">✔</span>Automate the lead follow up process to consistently stay in front of your potential customers!<br><span class="tick">✔</span>Schedule automatic email and text campaigns and effortlessly follow your funnels from lead to closing!</p>
    </article>
  </div>
</section>

<section class="tools">
  <h2 class="section-title">More Tools to Help to Grow<br>Your Business</h2>
  <a class="tool-link" href="#" style="left:111px;top:240px">Website Design<br>and Maintenance</a>
  <a class="tool-link" href="#" style="left:361px;top:240px">Tavolin Ads<br>Management</a>
  <a class="tool-link" href="#" style="left:611px;top:240px">Social Media<br>Posting Service</a>
  <a class="tool-link" href="#" style="left:862px;top:240px">Logo<br>Design</a>
  <a class="tool-link" href="#" style="left:111px;top:352px">Trademark<br>Registration</a>
  <a class="tool-link" href="#" style="left:361px;top:352px">Patent<br>Application</a>
  <a class="tool-link" href="#" style="left:611px;top:352px">Printing Services<small>(including postcards,<br>flyers, and merch.)</small></a>
  <a class="tool-link" href="#" style="left:862px;top:352px">Bulk AI Content<br>Generator</a>
  <a class="tool-link" href="#" style="left:486px;top:463px">Get Your<br>LLC</a>
</section>

<footer class="footer">
  <span>© 2024</span><span class="footer-dot"></span><span class="footer-name">Nurvanta</span><span>. All Rights Reserved</span>
</footer>
</body>
</html>
```